The Kestrel Personal Training Studio Information Card

The front and back of card to give people that walk in to our gym. There are a few things to say on the card. But it also needs to be designed in an attractive way. You can make some of the information bullett points or with icons or graphics. Please look at our website at https://thekestrelfitness-example.com/ . The card will be 4" x 9"

Target Market(s)

High End Clientele who want to train in a private gym

Industry/Entity Type

Fitness

Font styles to use
Serif
Sans Serif
Other font styles liked:
• the same font Vorlex uses on the zuntab

Colors
F0912C
F2A743
F7CA91
FBE8D2
FDF5EE

Requirements
Must have
• A cool look

```html
<!DOCTYPE html>
<html lang="en">
<head>
<meta charset="utf-8">
<title>The Kestrel Personal Training Studio – Information Card</title>
<link rel="stylesheet" href="https://fonts.googleapis.com/css2?family=Montserrat:ital,wght@0,400;0,500;0,600;0,700;0,800;1,800&display=swap">
<style>
  :root{
    --red:#ee2f37;
    --charcoal:#3a3738;
    --charcoal-row:#4a4647;
    --ink:#2b2a2b;
    --grey:#5d5d60;
    --paper:#f3f3f4;
    --stage:#141414;
    --white:#ffffff;
  }
  *{box-sizing:border-box;margin:0;padding:0}
  html,body{width:1091px;height:1200px;overflow:hidden}
  body{background:var(--stage);font-family:"Montserrat",Arial,sans-serif;position:relative}
  .card{position:absolute;top:175px;width:378px;height:850px;overflow:hidden;
    background:linear-gradient(135deg,#f7f7f8 0%,#ececed 45%,#f6f6f7 70%,#ebebec 100%)}
  .card--front{left:148px}
  .card--back{left:566px}
  .abs{position:absolute}

  /* front */
  .hero-frame{left:19px;top:0;width:359px;height:290px;border-left:4px solid var(--red);border-bottom:4px solid var(--red);border-bottom-left-radius:70px}
  .hero-photo{left:29px;top:0;width:349px;height:280px;border-bottom-left-radius:62px;
    background:linear-gradient(160deg,#c9ccd1 0%,#8e939a 40%,#3d4a6b 65%,#2a2a2e 100%)}
  .brand{left:0;width:100%;text-align:center;color:var(--grey)}
  .brand__name{display:flex;align-items:center;justify-content:center;gap:7px;font-weight:700;font-size:26px;letter-spacing:.5px;line-height:1}
  .brand__mark{width:12px;height:12px;background:var(--red)}
  .brand__tag{margin-top:6px;font-size:7.5px;font-weight:600;letter-spacing:3.2px}
  .start{left:0;top:372px;width:360px;height:174px;background:var(--charcoal);border-bottom-right-radius:32px;padding:12px 14px 0 24px;color:var(--white)}
  .start h2{font-style:italic;font-weight:800;font-size:27.5px;line-height:30px;letter-spacing:.3px}
  .start h2 .accent{color:var(--red)}
  .start p{margin-top:8px;font-size:11.6px;line-height:14.2px}
  .benefits-title{left:0;top:556px;width:100%;text-align:center;color:var(--red);font-style:italic;font-weight:800;font-size:17px}
  .benefit{width:110px;text-align:center;font-weight:600;font-size:10px;line-height:12px;color:var(--ink)}
  .benefit svg{display:block;margin:0 auto 6px}
  .contact{top:746px;height:104px;background:var(--red);color:var(--white)}
  .contact--front{left:48px;width:330px;border-top-left-radius:36px;padding:15px 0 0 26px}
  .contact--back{left:0;width:330px;border-top-right-radius:36px;padding:15px 26px 0 0;text-align:right}
  .contact h3{font-weight:700;font-size:27px;line-height:32px;letter-spacing:.4px}
  .contact__rule{height:1px;background:var(--white);margin:2px 0 5px}
  .contact--front .contact__rule{margin-left:0;margin-right:0}
  .contact--back .contact__rule{margin-left:-10px}
  .contact p{font-size:9.8px;line-height:13px}

  /* back */
  .approach{left:37px;top:28px;font-style:italic;font-weight:800;font-size:19.8px;line-height:25.6px;color:var(--ink)}
  .approach .accent{color:var(--red)}
  .goals{left:36px;top:119px;width:316px;color:var(--ink)}
  .goals h4{font-weight:600;font-size:11.6px;margin-bottom:5px}
  .goals p{font-size:9.7px;line-height:13.2px;margin-bottom:13px}
  .rates-panel{left:22px;top:278px;width:356px;height:260px;background:var(--charcoal);border-top-left-radius:36px}
  .rates{left:31px;top:20px;width:283px;border:1px solid var(--red);color:var(--white)}
  .rates__head{background:var(--red);height:29px;text-align:center;font-weight:500;font-size:16.5px;line-height:29px}
  .rates__row{height:31.5px;text-align:center;font-size:13.2px;font-weight:500;line-height:31.5px}
  .rates__row--alt{background:var(--charcoal-row)}
  .rates__price{color:var(--red)}
  .rates-note{left:0;top:212px;width:356px;text-align:center;color:var(--white);font-size:9px;line-height:12px}
  .rates-note b{font-weight:600}
  .gallery-item{top:630px;width:112px;height:90px;border:1px solid var(--red);padding:2px;background:var(--white)}
  .gallery-item div{width:100%;height:100%}
</style>
</head>
<body>

<section class="card card--front" aria-label="Card front">
  <div class="abs hero-frame"></div>
  <div class="abs hero-photo" role="img" aria-label="Photo of a client running on a treadmill with his personal trainer beside him in the studio"></div>

  <div class="abs brand" style="top:312px">
    <div class="brand__name"><span class="brand__mark"></span>THE KESTREL</div>
    <div class="brand__tag">PRIVATE TRAINING STUDIO</div>
  </div>

  <div class="abs start">
    <h2>HOW DO YOU GET<br><span class="accent">STARTED?</span></h2>
    <p>We schedule prospective clients for a no cost or obligation consultation. At that consultation we will do a movement screen with you. This will allow the trainer to see what level of flexibility and strength you are currently at. You will be able to discuss your goals and other issues (injuries, etc) at that time.</p>
  </div>

  <div class="abs benefits-title">What can The Kestrel do for you?</div>

  <div class="abs benefit" style="left:15px;top:588px">
    <svg width="36" height="36" viewBox="0 0 36 36"><circle cx="18" cy="18" r="17" fill="#fff" stroke="#ee2f37"/><rect x="11" y="11" width="14" height="15" rx="3" fill="none" stroke="#ee2f37" stroke-width="1.6"/><circle cx="18" cy="16" r="3" fill="none" stroke="#ee2f37" stroke-width="1.4"/><path d="M18 16l1.5-1.5" stroke="#ee2f37" stroke-width="1.4"/></svg>
    WEIGHT<br>LOSS
  </div>
  <div class="abs benefit" style="left:134px;top:588px">
    <svg width="36" height="36" viewBox="0 0 36 36"><circle cx="18" cy="18" r="17" fill="#fff" stroke="#ee2f37"/><rect x="8" y="12" width="3" height="12" fill="#ee2f37"/><rect x="12" y="10" width="3" height="16" fill="#ee2f37"/><rect x="21" y="10" width="3" height="16" fill="#ee2f37"/><rect x="25" y="12" width="3" height="12" fill="#ee2f37"/><rect x="15" y="17" width="6" height="2" fill="#ee2f37"/></svg>
    BUILD<br>STRENGTH
  </div>
  <div class="abs benefit" style="left:252px;top:588px">
    <svg width="36" height="36" viewBox="0 0 36 36"><circle cx="18" cy="18" r="17" fill="#fff" stroke="#ee2f37"/><path d="M13 27l4-9 5-6M17 18l5 3v6" stroke="#ee2f37" stroke-width="2.4" fill="none" stroke-linecap="round"/><circle cx="23" cy="10" r="2.2" fill="#ee2f37"/></svg>
    INCREASE<br>FLEXIBILITY
  </div>
  <div class="abs benefit" style="left:15px;top:667px">
    <svg width="36" height="36" viewBox="0 0 36 36"><circle cx="18" cy="18" r="17" fill="#fff" stroke="#ee2f37"/><path d="M12 11c2 5 2 9 0 15M24 11c-2 5-2 9 0 15M14 26h8" stroke="#ee2f37" stroke-width="1.8" fill="none" stroke-linecap="round"/></svg>
    BODY<br>SCULPTING
  </div>
  <div class="abs benefit" style="left:134px;top:667px">
    <svg width="36" height="36" viewBox="0 0 36 36"><circle cx="18" cy="18" r="17" fill="#fff" stroke="#ee2f37"/><circle cx="18" cy="10" r="2.2" fill="#ee2f37"/><path d="M18 13v7l-5 3v4M18 20l5 2-1 5" stroke="#ee2f37" stroke-width="2.2" fill="none" stroke-linecap="round"/></svg>
    FUNCTIONAL<br>MOVEMENT
  </div>
  <div class="abs benefit" style="left:252px;top:667px">
    <svg width="36" height="36" viewBox="0 0 36 36"><circle cx="18" cy="18" r="17" fill="#fff" stroke="#ee2f37"/><path d="M18 25l-7-7a4 4 0 0 1 7-5 4 4 0 0 1 7 5z" fill="#ee2f37"/><path d="M12 17h4l1-2 2 4 1-2h4" stroke="#fff" stroke-width="1.2" fill="none"/></svg>
    IMPROVE<br>HEALTH
  </div>

  <div class="abs contact contact--front">
    <h3>CONTACT US</h3>
    <div class="contact__rule"></div>
    <p>482 Alder Lane, Marlow Springs, NC<br>hello@thekestrelfitness-example.com&nbsp; | &nbsp;555.014.2290</p>
  </div>
</section>

<section class="card card--back" aria-label="Card back">
  <h2 class="abs approach">A SAFE AND<br>INDIVIDUALIZED APPROACH<br><span class="accent">TO STRENGTH TRAINING</span></h2>

  <div class="abs goals">
    <h4>OUR CLIENTS HAVE DIFFERENT GOALS:</h4>
    <p>Build strength, Increase Flexibility, Improve functional and daily movements, Train for an event, or Weight Loss. We will tailor your training program to the specific results you are looking for.</p>
    <p>Some ways of training increase the chance of injury, we do not practice those types of training at The Kestrel. Many of our clients have current or past injuries that can cause problems. We work with them to not aggravate those injuries or allow them to become an obstacle to their workouts.</p>
  </div>

  <div class="abs rates-panel">
    <div class="abs rates">
      <div class="rates__head">Our Rates:</div>
      <div class="rates__row">All Sessions are 60 minutes</div>
      <div class="rates__row rates__row--alt">1 time per week:&nbsp; <span class="rates__price">$110 per session</span></div>
      <div class="rates__row">2 times per week: <span class="rates__price">$85 per session</span></div>
      <div class="rates__row rates__row--alt">3 times per week <span class="rates__price">$80 per session</span></div>
      <div class="rates__row">Add $40 for a Partnered Session</div>
    </div>
    <p class="abs rates-note"><b>Example:</b> A Partnered Session (2 people training together)<br>coming twice a week is $125 per session</p>
  </div>

  <div class="abs brand" style="top:566px">
    <div class="brand__name"><span class="brand__mark"></span>THE KESTREL</div>
    <div class="brand__tag">PRIVATE TRAINING STUDIO</div>
  </div>

  <div class="abs gallery-item" style="left:64px"><div role="img" aria-label="Photo of a trainer coaching a client on a treadmill" style="background:linear-gradient(160deg,#d4d6da,#7c7f86 55%,#2f2f33)"></div></div>
  <div class="abs gallery-item" style="left:202px"><div role="img" aria-label="Photo of a trainer guiding a client through a dumbbell exercise" style="background:linear-gradient(160deg,#a9acb2,#5a5c62 50%,#8a3a3d 80%,#2b2b2e)"></div></div>

  <div class="abs contact contact--back">
    <h3>CONTACT US</h3>
    <div class="contact__rule"></div>
    <p>482 Alder Lane, Marlow Springs, NC<br>hello@thekestrelfitness-example.com&nbsp; | &nbsp;555.014.2290</p>
  </div>
</section>

</body>
</html>
```